Digital Album Artwork - Corvina Piano Tribute

I'd like a digital album cover designed . The album will feature piano instrumental background music of Corvina's hits.

Sample tracks and style of my music are (FYI)
https://tunewharf.example/tobyhaskellpianist/sets/corvina-piano-tribute

Previous album covers that I have selected from Sketch Quarry artists are
https://melodybin.example/au/artist/toby-haskell/4820193756

```html
<!DOCTYPE html>
<html lang="en">
<head>
<meta charset="utf-8">
<title>Piano Instrumental – Corvina's hits</title>
<link rel="stylesheet" href="https://fonts.googleapis.com/css2?family=Great+Vibes&family=Raleway:wght@400;500&display=swap">
<style>
  :root {
    --page-bg: #ffffff;
    --navy-deep: #0f1426;
    --navy-mid: #1e2745;
    --slate-light: #7d8299;
    --slate-soft: #a9adbd;
    --title-ink: #ffffff;
    --mark-ink: #121212;
  }
  html, body {
    margin: 0;
    padding: 0;
    width: 1200px;
    height: 1200px;
    overflow: hidden;
    background: var(--page-bg);
  }
  .cover {
    position: relative;
    width: 1200px;
    height: 1200px;
    background: var(--page-bg);
  }
  .cover__artwork {
    position: absolute;
    left: 92px;
    top: 92px;
    width: 1016px;
    height: 1016px;
    overflow: hidden;
    background:
      radial-gradient(ellipse 70% 45% at 35% 80%, rgba(169,173,189,0.55) 0%, rgba(125,130,153,0.25) 45%, rgba(0,0,0,0) 75%),
      linear-gradient(160deg, var(--navy-deep) 0%, var(--navy-mid) 45%, #3a4160 70%, #262c46 100%);
  }
  .cover__photo {
    position: absolute;
    inset: 0;
  }
  .cover__title {
    position: absolute;
    left: 0;
    right: 0;
    top: 205px;
    margin: 0;
    text-align: center;
    color: var(--title-ink);
    font-weight: 400;
  }
  .cover__title-script {
    display: block;
    font-family: "Great Vibes", cursive;
    font-size: 86px;
    line-height: 1;
    padding-left: 48px;
  }
  .cover__title-sans {
    display: block;
    font-family: "Raleway", sans-serif;
    font-size: 60px;
    line-height: 1;
    margin-top: 22px;
    margin-right: 92px;
  }
  .artist-mark {
    position: absolute;
    left: 276px;
    top: 856px;
    display: flex;
    align-items: center;
    gap: 20px;
  }
  .artist-mark__dot {
    width: 100px;
    height: 100px;
    border-radius: 50%;
    background: var(--mark-ink);
  }
  .artist-mark__name {
    font-family: "Raleway", sans-serif;
    font-weight: 500;
    font-size: 42px;
    letter-spacing: 0.5px;
    color: var(--mark-ink);
  }
</style>
</head>
<body>
  <main class="cover">
    <section class="cover__artwork">
      <div class="cover__photo" role="img" aria-label="Close-up photograph of piano keys in dim blue light"></div>
      <h1 class="cover__title">
        <span class="cover__title-script">Piano Instrumental</span>
        <span class="cover__title-sans">Corvina's hits</span>
      </h1>
      <div class="artist-mark">
        <span class="artist-mark__dot"></span>
        <span class="artist-mark__name">TOBYHASKELL</span>
      </div>
    </section>
  </main>
</body>
</html>
```